professional business card design

Business card design. Photos have been uploaded and i am open to the designer choosing which photos to use. Would like the card to be mostyly in a grey scale design with black, whites, silver & grey colours. I have added copy of our flyer as would like on the back side of card our services to be listed. Do not use any bright colurs such as blue red green or yellow. i need to be able to edit the phone number and naem in the final card design submitted.

Target Market(s)

Clients

Industry/Entity Type

earhmovibng and transport

Contact Information for Business Card

Director Name, address, email, phone number and services

Colors

Designer to choose only greyscale colors for use in the design.

Requirements
Should not have
• no yellow, red, blue or green

```html
<!DOCTYPE html>
<html lang="en">
<head>
<meta charset="utf-8">
<title>Daniel Hart – Business Card</title>
<link href="https://fonts.googleapis.com/css2?family=Montserrat:wght@400;500;700&display=swap" rel="stylesheet">
<style>
  :root{
    --bg:#4a3324;
    --card:#151515;
    --accent:#c9c9c9;
    --ink:#ffffff;
    --photo-a:#3b3b3b;
    --photo-b:#a9a9a9;
  }
  *{margin:0;padding:0;box-sizing:border-box}
  html,body{width:1200px;height:848px;overflow:hidden}
  body{background:var(--bg);font-family:"Montserrat",sans-serif;color:var(--ink);position:relative}
  .card{position:absolute;left:289px;width:599px;height:326px;background:var(--card);border-radius:17px;box-shadow:0 6px 18px rgba(0,0,0,.45)}
  .card--front{top:76px}
  .card--back{top:443px}
  .photo{position:absolute;border-radius:6px;background:linear-gradient(135deg,var(--photo-a),var(--photo-b) 55%,#5c5c5c)}
  .front-photo{left:42px;top:86px;width:290px;height:155px}
  .divider{position:absolute;left:342px;top:73px;width:2px;height:180px;background:var(--accent)}
  .details{position:absolute;left:357px;top:68px}
  .name{font-weight:700;font-size:25.5px;color:var(--accent);letter-spacing:.3px;line-height:1.2}
  .role{font-size:15.5px;margin-top:3px;letter-spacing:.3px}
  .contacts{list-style:none;margin-top:18px}
  .contacts li{font-size:15.5px;line-height:21.5px;display:flex;align-items:center;gap:6px}
  .contacts svg{width:13px;height:13px;flex:none}
  .depot{font-size:15.5px;line-height:21.5px;margin-top:12px}
  .tagline{position:absolute;left:0;right:0;top:267px;text-align:center;font-size:15.5px;line-height:21.5px}
  .back-photo-left{left:21px;top:19px;width:226px;height:116px}
  .back-photo-right{left:281px;top:19px;width:297px;height:108px}
  .services-title{position:absolute;left:189px;top:140px;width:221px;height:33px;border:2px solid var(--accent);border-radius:17px;text-align:center;font-weight:400;font-size:21.5px;line-height:29px;letter-spacing:.5px}
  .services{position:absolute;list-style:none}
  .services--left{left:22px;top:179px}
  .services--right{left:370px;top:181px}
  .services li{font-size:15.5px;line-height:21.5px;display:flex;align-items:center;gap:8px}
  .services li::before{content:"";width:11px;height:11px;border-radius:50%;background:var(--accent);flex:none}
</style>
</head>
<body>
  <section class="card card--front">
    <div class="photo front-photo" role="img" aria-label="Two road train trucks, silver and black"></div>
    <div class="divider"></div>
    <div class="details">
      <h1 class="name">DANIEL HART</h1>
      <p class="role">Managing Director</p>
      <ul class="contacts">
        <li><svg viewBox="0 0 16 16"><path fill="#c9c9c9" d="M3 2h3l1.5 3.5-2 1.2a8 8 0 0 0 3.8 3.8l1.2-2L14 10v3a1 1 0 0 1-1 1A11 11 0 0 1 2 3a1 1 0 0 1 1-1z"/></svg>123 456 789</li>
        <li><svg viewBox="0 0 16 16"><rect x="1" y="3" width="14" height="10" rx="1" fill="#c9c9c9"/><path d="M1.5 3.5 8 8.5l6.5-5" stroke="#151515" stroke-width="1.4" fill="none"/></svg>info@yourgmail.com</li>
        <li><svg viewBox="0 0 16 16"><circle cx="8" cy="8" r="6.5" fill="#c9c9c9"/><path d="M4 5c2 0 2 2 4 2s1 3-1 4M10 3c0 2 2 2 3 4" stroke="#151515" stroke-width="1.2" fill="none"/></svg>www.yourwebsite.com</li>
      </ul>
      <p class="depot">Depot: Lot 114 Redgum Hill<br>Road Marlow Flats</p>
    </div>
    <p class="tagline">We offer a large range of services not listed so<br>Call us today for a personalised quote to suit your needs.</p>
  </section>

  <section class="card card--back">
    <div class="photo back-photo-left" role="img" aria-label="Two road train trucks, silver and black"></div>
    <div class="photo back-photo-right" role="img" aria-label="Black prime mover hauling a road train of white tankers"></div>
    <h2 class="services-title">OUR SERVICES</h2>
    <ul class="services services--left">
      <li>Over Size Loads / Hot Shot Loads</li>
      <li>Heavy Vehicle Recovery Services</li>
      <li>Potable Water Deliveries</li>
      <li>Road Building / Maintenance</li>
      <li>Earthworks</li>
      <li>Sand &amp; Mental Supply &amp; Cartage</li>
    </ul>
    <ul class="services services--right">
      <li>Road Train Tippers</li>
      <li>Road Train Tankers</li>
      <li>Road Rrain Flat Tops</li>
      <li>Drop Deck Trailers</li>
      <li>Mine Site accredited</li>
      <li>equipment &amp; Operattors</li>
    </ul>
  </section>
</body>
</html>
```